Pool Website

Need a simple front page and one internal page for a pool construction website. Please read the Must Have section for info. We uploaded 2 logos, one with color and one black and white. The colors you use in the logo can be changed, we used Century Gothic for the typing under the logo.

Nice clean design. The main back behind the site can be any color but we want the content back ground to be white.

We want a scrolling photo gallery (it doesn't have to scroll in your sample just know that's what we are envisioning) on the front page and the menu, and maybe a couple of photos down below to be clicked on such as this http://www.dellmorepools.example/

The 2ndary page would still have a header and menu and some type of cool design. Could be similar to this http://www.dellmorepools.example/about-us/awards.html

Also some other designs they like are here http://www.trelvacraft.example/14-examples-of-clean-modern-website-design-inspiration/ I realize not all of these could have a image scroller on the front page which is fine.

Please do not copy their site exactly though it must be different.

For now you can just use sample stock photography for your photos for the design but ultimately we will swap them out for our own photos so there will not be a need to purchase stock photography of pools.

Menus will include Home - About - Services - Gallery - Contact - Blog

The current site is http://www.gilesfentonpools.example/ we do not want it to look anything like this. It's way too dark and just not professional looking. We want this new site to look very slick and professional.

We also want a space for social networking logos etc.

I have also attached 2 zip files that contain photos that may be used in the design. You do not have to use them all but you are welcome to use a few. Most will be put in the photo gallery.

Colors: Blues, white, grays, black, etc.
Updates

Added several photos that can be used in the design. Obviously you do not have to use them all most will be in the photo gallery but you're welcome to use some for your design. 

Target Market(s)

People with money for residential pools or companies that want corporate pools. Are target location is Miami and California

Industry/Entity Type

Construction

Font styles to use
Serif
Sans Serif

Requirements
Must have
• Nice clean design. The main back behind the site can be any color but we want the content back ground to be white.

```html
<!DOCTYPE html>
<html lang="en">
<head>
<meta charset="utf-8">
<title>Giles Fenton Pools</title>
<link href="https://fonts.googleapis.com/css2?family=Fira+Sans:ital,wght@0,400;0,500;1,400&family=PT+Sans:wght@400&family=Arimo:ital,wght@0,400;0,700;1,400&display=swap" rel="stylesheet">
<style>
:root{
  --navy:#1c2378;
  --teal:#00b9c9;
  --text:#555;
  --heading:#333;
  --line:#d4d4d4;
  --footer:#474747;
  --footer-bottom:#3a3a3a;
  --footer-text:#d8d8d8;
  --icon-grey:#9a9a9a;
  --white:#fff;
}
*{margin:0;padding:0;box-sizing:border-box}
html,body{width:1045px;height:1200px;overflow:hidden;background:var(--white)}
body{position:relative;font-family:"Fira Sans",sans-serif;color:var(--text)}
.abs{position:absolute}
.top-rule{left:0;top:0;width:1045px;height:2px;background:var(--navy)}
.brand{left:157px;top:18px;display:flex;align-items:center;gap:8px}
.brand-mark{width:22px;height:22px;background:var(--navy)}
.brand-name{font-family:"Fira Sans",sans-serif;font-size:16px;font-weight:500;color:var(--navy);line-height:1.1;width:80px}
.nav a{position:absolute;top:29px;height:23px;line-height:23px;font-size:12px;color:#333;text-decoration:none;transform:translateX(-50%);white-space:nowrap}
.nav a.active{background:var(--navy);color:var(--white);border-radius:4px;width:52px;text-align:center}
.hero{left:0;top:78px;width:1045px;height:296px;background:linear-gradient(160deg,#3c4a3a 0%,#6e7f8e 22%,#5aa9d6 48%,#8fd0ea 62%,#6c8a4c 82%,#3d4a2e 100%)}
.hero-arrow{top:196px}
.offer{left:0;top:374px;width:1045px;height:41px;background:var(--teal);color:var(--white);font-family:"PT Sans",sans-serif;font-size:20px;line-height:41px;text-align:center}
.services-arrow{top:449px}
.service{top:436px;width:180px;transform:translateX(-50%);text-align:center}
.service-icon{display:block;margin:0 auto}
.service h3{font-size:12.5px;font-weight:400;color:#333;margin-top:10px;letter-spacing:.2px}
.service p{font-size:11px;line-height:14.5px;color:#666;margin-top:5px}
.service a{display:block;font-size:9.5px;color:var(--navy);text-decoration:none;margin-top:4px}
.section-title{font-family:"Arimo",sans-serif;font-weight:700;font-size:14.5px;color:var(--heading);display:flex;align-items:center;gap:8px;white-space:nowrap}
.section-title::after{content:"";flex:1;height:1px;background:var(--line)}
.welcome-title{left:164px;top:624px;width:352px}
.why-title{left:529px;top:625px;width:355px}
.tagline{left:164px;top:655px;font-family:"Arimo",sans-serif;font-style:italic;font-size:11.5px;color:#444}
.features{left:163px;top:676px;list-style:none;font-size:10.5px;color:#555}
.features li{height:20px;line-height:14px;padding-left:8px;position:relative}
.features li::before{content:"";position:absolute;left:0;top:4px;border-left:4px solid #555;border-top:3px solid transparent;border-bottom:3px solid transparent}
.intro{left:166px;top:757px;width:350px;height:84px;overflow:hidden;font-size:10.5px;line-height:14px;color:#555}
.read-more{font-size:9.5px;color:var(--navy);text-decoration:none}
.welcome-more{left:164px;top:852px}
.accordion{left:530px;width:355px}
.acc-head{height:21px;border:1px solid #c8c8c8;font-family:"Arimo",sans-serif;font-size:11px;color:#555;line-height:19px;padding-left:10px;position:relative;margin-bottom:7px}
.acc-head .plus{position:absolute;right:10px;top:0;font-size:13px;color:#777}
.acc-body{font-family:"Arimo",sans-serif;font-size:10.5px;line-height:14.5px;color:#555;padding:6px 2px 0;height:55px}
.footer{left:0;top:900px;width:1045px;height:243px;background:var(--footer)}
.footer-title{font-size:13px;color:var(--white)}
.gallery-title{left:163px;top:921px}
.thumb{width:45px;height:38px;border:2px solid #9a9a9a}
.address-title{left:474px;top:923px}
.address{left:473px;top:954px;font-size:9.5px;color:var(--footer-text);line-height:16px}
.address dt{float:left;width:28px;clear:left}
.address dd{margin-left:28px}
.map{left:470px;top:1033px;width:219px;height:68px;border:3px solid #8a8a8a;background:linear-gradient(135deg,#dfe4ea,#cfd8e0 60%,#bcd0e6)}
.footer-brand{left:773px;top:940px;display:flex;align-items:center;gap:8px}
.footer-brand .brand-mark{background:var(--teal)}
.footer-brand .brand-name{color:var(--white);width:80px}
.follow{left:773px;top:1030px;width:110px;text-align:center;font-family:"Arimo",sans-serif;font-weight:700;font-style:italic;font-size:11.5px;color:#ddd}
.social{top:1056px;width:30px;height:30px;border-radius:50%;border:2px solid #cfcfcf}
.social.one{left:780px;background:#2a5aa8}
.social.two{left:813px;background:#4fb8e0}
.social.three{left:846px;background:#2f6fb5}
.footer-bar{left:0;top:1143px;width:1045px;height:57px;background:var(--footer-bottom)}
.footer-links{left:0;top:1155px;width:1045px;text-align:center;font-family:"Arimo",sans-serif;font-size:9.5px;color:#aaa}
.footer-links a{color:#aaa;text-decoration:none}
.footer-links a.active{color:var(--white)}
.footer-links span{margin:0 4px}
.copyright{left:0;top:1175px;width:1045px;text-align:center;font-family:"Arimo",sans-serif;font-size:9.5px;color:#ccc}
</style>
</head>
<body>
<div class="abs top-rule"></div>

<header>
  <div class="abs brand"><span class="brand-mark"></span><span class="brand-name">Giles Fenton Pools</span></div>
  <nav class="nav">
    <a class="active" href="#" style="left:497px">Home</a>
    <a href="#" style="left:581px">About Us</a>
    <a href="#" style="left:672px">Services</a>
    <a href="#" style="left:757px">Gallery</a>
    <a href="#" style="left:849px">Contact Us</a>
  </nav>
</header>

<section class="abs hero" role="img" aria-label="Photo of a luxury pool with fountain planters, palm trees and lake view"></section>
<svg class="abs hero-arrow" style="left:150px" width="16" height="32" viewBox="0 0 16 32"><path d="M13 2 3 16l10 14" fill="none" stroke="#fff" stroke-width="3"/></svg>
<svg class="abs hero-arrow" style="left:882px" width="16" height="32" viewBox="0 0 16 32"><path d="M3 2l10 14L3 30" fill="none" stroke="#fff" stroke-width="3"/></svg>

<div class="abs offer">SPECIAL OFFER: Free Estimates &amp; Design Consults LIFETIME WARRANTY AVAILABLE</div>

<svg class="abs services-arrow" style="left:151px" width="12" height="30" viewBox="0 0 12 30"><path d="M10 1 2 15l8 14" fill="none" stroke="#888" stroke-width="1.2"/></svg>
<svg class="abs services-arrow" style="left:884px" width="12" height="30" viewBox="0 0 12 30"><path d="M2 1l8 14-8 14" fill="none" stroke="#888" stroke-width="1.2"/></svg>

<section class="services">
  <div class="abs service" style="left:247px">
    <svg class="service-icon" width="58" height="58" viewBox="0 0 58 58"><circle cx="29" cy="29" r="27" fill="#fff" stroke="var(--teal)" stroke-width="2.5"/><circle cx="29" cy="23" r="5" fill="#444"/><g stroke="#444" stroke-width="1.5"><path d="M29 13v3M29 30v-1M19 23h3M36 23h3M22 16l2 2M36 16l-2 2"/></g><g fill="none" stroke="#444" stroke-width="1.6"><path d="M15 33q3.5-3 7 0t7 0 7 0 7 0"/><path d="M15 38q3.5-3 7 0t7 0 7 0 7 0"/><path d="M15 43q3.5-3 7 0t7 0 7 0 7 0"/></g></svg>
    <h3>Commercial Pool Installation</h3>
    <p>Lorem ipsum dolor sit amet, consectetuer adipiscing elit, se diam nonummy nibh euismod</p>
    <a href="#">Read More...</a>
  </div>
  <div class="abs service" style="left:433px">
    <svg class="service-icon" width="58" height="58" viewBox="0 0 58 58"><circle cx="29" cy="29" r="27" fill="#fff" stroke="var(--icon-grey)" stroke-width="2.5"/><circle cx="36" cy="21" r="3.5" fill="#444"/><path d="M17 31l9-7 6 3-4 4" fill="none" stroke="#444" stroke-width="3"/><g fill="none" stroke="#444" stroke-width="1.6"><path d="M15 35q3.5-3 7 0t7 0 7 0 7 0"/><path d="M15 40q3.5-3 7 0t7 0 7 0 7 0"/></g></svg>
    <h3>Pool Maintenance</h3>
    <p>Lorem ipsum dolor sit amet, consectetuer adipiscing elit, se diam nonummy nibh euismod</p>
    <a href="#">Read More...</a>
  </div>
  <div class="abs service" style="left:618px">
    <svg class="service-icon" width="58" height="58" viewBox="0 0 58 58"><circle cx="29" cy="29" r="27" fill="#fff" stroke="var(--icon-grey)" stroke-width="2.5"/><ellipse cx="29" cy="30" rx="11" ry="5" fill="none" stroke="#444" stroke-width="2.5"/><circle cx="31" cy="20" r="3" fill="#444"/><g fill="none" stroke="#444" stroke-width="1.6"><path d="M15 38q3.5-3 7 0t7 0 7 0 7 0"/><path d="M15 43q3.5-3 7 0t7 0 7 0 7 0"/></g></svg>
    <h3>Swimming PoolInstallation</h3>
    <p>Lorem ipsum dolor sit amet, consectetuer adipiscing elit, se diam nonummy nibh euismod</p>
    <a href="#">Read More...</a>
  </div>
  <div class="abs service" style="left:803px">
    <svg class="service-icon" width="58" height="58" viewBox="0 0 58 58"><circle cx="29" cy="29" r="27" fill="#fff" stroke="var(--icon-grey)" stroke-width="2.5"/><g stroke="#444" stroke-width="2.5" stroke-linecap="round"><path d="M21 14l16 17M37 14 21 31"/></g><g fill="none" stroke="#444" stroke-width="1.6"><path d="M15 36q3.5-3 7 0t7 0 7 0 7 0"/><path d="M15 41q3.5-3 7 0t7 0 7 0 7 0"/></g></svg>
    <h3>Pool Renovation</h3>
    <p>Lorem ipsum dolor sit amet, consectetuer adipiscing elit, se diam nonummy nibh euismod</p>
    <a href="#">Read More...</a>
  </div>
</section>

<section class="welcome">
  <h2 class="abs section-title welcome-title">Welcome to Giles Fenton Pools</h2>
  <p class="abs tagline">Giles Fenton Pool Contracting, Inc., your Ultimate Dealer !</p>
  <ul class="abs features">
    <li>Full Service Pool Company</li>
    <li>Residential and Commercial Pools in South Florida</li>
    <li>Maintenance, Repairs and Renovations</li>
    <li>Impressive Showroom (near Harlow Road and Keel Road)</li>
  </ul>
  <p class="abs intro">That's just some of the services we offer at Giles Fenton Pool Contracting, Inc. you'll find quality, selection, and innovative planning and construction no matter what your pool needs may be. Some of our clients are developers including Brenmoor Homes, T.L.K. Communities, Ashford Development, Corvane Homes and Lindell Homes ... but the customer is you during the design and construction of your new pool.</p>
  <a class="abs read-more welcome-more" href="#">Read More...</a>
</section>

<section class="why">
  <h2 class="abs section-title why-title">Why Choose Us?</h2>
  <div class="abs accordion" style="top:658px">
    <div class="acc-head">Free Estimates</div>
    <p class="acc-body">Lorem ipsum dolor sit amet, consectetuer adipiscing elit, sed diam nonummy nibh euismod tincidunt ut laoreet dolore magna aliquam erat volutpat. Ut wisi enim ad minim veniam, quis nostrud exerci tation.</p>
    <div class="acc-head">Family Owned since 1979<span class="plus">+</span></div>
    <div class="acc-head">National Pool Builders Guild Member<span class="plus">+</span></div>
    <div class="acc-head">Awarded over 75 NPBG Awards<span class="plus">+</span></div>
    <div class="acc-head">Free Design Consults Available<span class="plus">+</span></div>
  </div>
</section>

<footer>
  <div class="abs footer"></div>
  <h4 class="abs footer-title gallery-title">Our Gallery</h4>
  <div class="abs thumb" style="left:163px;top:957px;background:linear-gradient(#7a9a6a,#5ab0d8)" role="img" aria-label="Pool photo thumbnail"></div>
  <div class="abs thumb" style="left:225px;top:957px;background:linear-gradient(#6e8a5a,#3a7fb0)" role="img" aria-label="Pool photo thumbnail"></div>
  <div class="abs thumb" style="left:287px;top:957px;background:linear-gradient(#a9cfe6,#6fb6dc)" role="img" aria-label="Pool photo thumbnail"></div>
  <div class="abs thumb" style="left:348px;top:957px;background:linear-gradient(#4f6a44,#4aa6d0)" role="img" aria-label="Pool photo thumbnail"></div>
  <div class="abs thumb" style="left:163px;top:1012px;background:linear-gradient(#8aa07a,#3f7fa6)" role="img" aria-label="Pool photo thumbnail"></div>
  <div class="abs thumb" style="left:225px;top:1012px;background:linear-gradient(#7a8f9c,#4a7f9e)" role="img" aria-label="Pool photo thumbnail"></div>
  <div class="abs thumb" style="left:287px;top:1012px;background:linear-gradient(#7d8a6e,#4d8fb8)" role="img" aria-label="Pool photo thumbnail"></div>
  <div class="abs thumb" style="left:348px;top:1012px;background:linear-gradient(#1c2430,#3a6fa0)" role="img" aria-label="Night pool photo thumbnail"></div>
  <div class="abs thumb" style="left:163px;top:1063px;background:linear-gradient(#c9c2b0,#3f8fc8)" role="img" aria-label="Pool photo thumbnail"></div>
  <div class="abs thumb" style="left:225px;top:1063px;background:linear-gradient(#6f8a5e,#3a8ab8)" role="img" aria-label="Pool photo thumbnail"></div>
  <div class="abs thumb" style="left:287px;top:1063px;background:linear-gradient(#8fa5b0,#5fa8cc)" role="img" aria-label="Pool photo thumbnail"></div>
  <div class="abs thumb" style="left:348px;top:1063px;background:linear-gradient(#8ab0c8,#5a8a5a)" role="img" aria-label="Pool photo thumbnail"></div>

  <h4 class="abs footer-title address-title">Address</h4>
  <dl class="abs address">
    <dt>Ad:</dt><dd>2410 NW 48 Court<br>Coral Bay, Florida 33999</dd>
    <dt>Tel:</dt><dd>555-014-2297</dd>
    <dt>Fax:</dt><dd>555-014-2297</dd>
  </dl>
  <div class="abs map" role="img" aria-label="Street map showing the showroom location"></div>

  <div class="abs footer-brand"><span class="brand-mark"></span><span class="brand-name">Giles Fenton Pools</span></div>
  <p class="abs follow">Follow Us On</p>
  <a class="abs social one" href="#" aria-label="Social network one"></a>
  <a class="abs social two" href="#" aria-label="Social network two"></a>
  <a class="abs social three" href="#" aria-label="Social network three"></a>

  <div class="abs footer-bar"></div>
  <nav class="abs footer-links">
    <a class="active" href="#">Home</a><span>|</span><a href="#">About Us</a><span>|</span><a href="#">Services</a><span>|</span><a href="#">Gallery</a><span>|</span><a href="#">Contact Us</a>
  </nav>
  <p class="abs copyright">Copyright © 2014 Giles Fenton Pools.&nbsp; All Rights Reserved.</p>
</footer>
</body>
</html>
```